Plumbing Company After Business Card

Business card for a plumbing business that offers a variety of plumbing services including maintenance, domestic and commercial plumbing. My main focus is to offer high quality professional service. A logo on the card would be ideal. Any other questions feel free to email. Cheers

Looking for something modern and upmarket with preferably a matte black background

Business name is Keystone Plumbing and Gas

Industry/Entity Type

Plumbing

Contact Information for Business Card

Keystone Plumbing and Gas
Marcus Thornell
0427915368
14 Corrigan Road, Elmvale 3561
keystoneplumbing@mailbay.com.au
ABN 52 647 183 925

Font styles to use
Sans Serif

Colors
1b1b1b
ffffff
3377b5

Requirements
Must have
• Domestic
• Commercial
• Maintenance

```html
<!DOCTYPE html>
<html lang="en">
<head>
<meta charset="UTF-8">
<title>Keystone Plumbing and Gas – Business Card</title>
<link rel="stylesheet" href="https://fonts.googleapis.com/css2?family=Lato:wght@300;400;900&display=swap">
<style>
  :root {
    --ink: #1b1b1b;
    --paper: #ffffff;
    --brand-blue: #3377b5;
    --backdrop: #d9d9d9;
  }
  * { box-sizing: border-box; margin: 0; padding: 0; }
  html, body { width: 1200px; height: 900px; overflow: hidden; }
  body {
    background: var(--backdrop);
    font-family: "Lato", sans-serif;
    position: relative;
  }
  .card {
    position: absolute;
    width: 700px;
    height: 400px;
    overflow: hidden;
    box-shadow: 0 6px 18px rgba(0,0,0,0.25);
  }
  .card-back { left: 440px; top: 40px; background: var(--ink); }
  .card-front { left: 60px; top: 460px; background: var(--paper); }

  .brand {
    position: absolute;
    display: flex;
    align-items: center;
    gap: 18px;
  }
  .brand-square {
    width: 64px; height: 64px;
    background: var(--brand-blue);
    flex: none;
  }
  .brand-name {
    font-weight: 900;
    text-transform: uppercase;
    line-height: 1.0;
    letter-spacing: 1px;
  }
  .card-back .brand { left: 190px; top: 95px; }
  .card-back .brand-name { color: var(--paper); font-size: 34px; }

  .services {
    position: absolute;
    left: 50px; right: 50px; bottom: 70px;
    display: flex;
    justify-content: space-between;
    list-style: none;
  }
  .services li {
    color: var(--brand-blue);
    font-weight: 400;
    font-size: 19px;
    letter-spacing: 1.5px;
    text-transform: uppercase;
  }

  .card-front .brand { left: 40px; top: 30px; }
  .card-front .brand-name { color: var(--ink); font-size: 28px; }
  .person { position: absolute; left: 40px; top: 118px; }
  .person-name { color: var(--brand-blue); font-size: 26px; font-weight: 400; }
  .person-role { color: var(--ink); font-size: 14px; margin-top: 2px; }

  .waves { position: absolute; left: 0; top: 0; width: 700px; height: 400px; }

  .contact {
    position: absolute;
    right: 36px; bottom: 22px;
    text-align: right;
    color: var(--paper);
    font-size: 16px;
    line-height: 1.3;
    list-style: none;
  }
  .contact li { display: flex; justify-content: flex-end; align-items: center; gap: 10px; }
  .contact .gap { margin-top: 8px; }
  .contact svg { width: 16px; height: 16px; fill: var(--brand-blue); flex: none; }
</style>
</head>
<body>

<section class="card card-back" aria-label="Card back">
  <div class="brand">
    <span class="brand-square"></span>
    <span class="brand-name">Keystone<br>Plumbing<br>and Gas</span>
  </div>
  <ul class="services">
    <li>Domestic</li>
    <li>Commercial</li>
    <li>Maintenance</li>
  </ul>
</section>

<section class="card card-front" aria-label="Card front">
  <svg class="waves" viewBox="0 0 700 400" aria-hidden="true">
    <path fill="var(--brand-blue)" d="M0,178 C110,208 230,226 350,226 C230,240 110,232 0,204Z"/>
    <path fill="var(--brand-blue)" d="M300,226 C420,214 600,160 700,70 L700,94 C600,182 420,232 300,234Z"/>
    <path fill="var(--ink)" d="M0,218 C160,266 380,240 500,212 C590,192 660,146 700,104 L700,116 C660,158 590,206 500,226 C380,254 160,282 0,234Z"/>
    <path fill="var(--ink)" d="M0,248 C170,292 380,270 500,240 C590,218 660,170 700,130 L700,400 L0,400Z"/>
  </svg>

  <div class="brand">
    <span class="brand-square"></span>
    <span class="brand-name">Keystone<br>Plumbing and Gas</span>
  </div>
  <div class="person">
    <p class="person-name">Marcus Thornell</p>
    <p class="person-role">Owner</p>
  </div>

  <ul class="contact">
    <li>ABN 52 647 183 925</li>
    <li class="gap">14 Corrigan Road</li>
    <li>Elmvale 3561</li>
    <li class="gap">0427 915 368
      <svg viewBox="0 0 24 24" aria-label="Phone"><path d="M6.6 10.8a15.1 15.1 0 0 0 6.6 6.6l2.2-2.2a1 1 0 0 1 1-.25 11.4 11.4 0 0 0 3.6.57 1 1 0 0 1 1 1V20a1 1 0 0 1-1 1A17 17 0 0 1 3 4a1 1 0 0 1 1-1h3.5a1 1 0 0 1 1 1c0 1.250.2 2.45.57 3.57a1 1 0 0 1-.25 1Z"/></svg>
    </li>
    <li>keystoneplumbing@mailbay.com.au
      <svg viewBox="0 0 24 24" aria-label="Email"><path d="M2 5h20v14H2Zm2 2v.5l8 5 8-5V7Zm0 2.8V17h16V9.8l-8 5Z"/></svg>
    </li>
  </ul>
</section>

</body>
</html>
```